Faithful in the Small...Powerful together

Capital Campaign for Meadowlight Church...need it engaging..spiritually based with pics of the community etc...

Target Market(s)

church congregation and sphere of influence

Industry/Entity Type

religious

Colors
EB3D1F
EC4F4E
F09395
F8D3D4
FCEDEE

Requirements
Must have
• tier levels..engaging scripture and photos

```html
<!DOCTYPE html>
<html lang="en">
<head>
<meta charset="utf-8">
<title>Meadowlight Church – Capital Campaign Brochure</title>
<link href="https://fonts.googleapis.com/css2?family=Montserrat:wght@400;500;600;700;800&family=Great+Vibes&display=swap" rel="stylesheet">
<style>
  :root{
    --bg:#8a8a8a;
    --red:#EB3D1F;
    --red-soft:#EC4F4E;
    --orange:#F4921F;
    --pink:#F09395;
    --blush:#F8D3D4;
    --paper:#ffffff;
    --paper-grey:#f3f3f4;
    --ink:#2b2b2b;
    --ink-soft:#555;
    --black:#0b0b0c;
    --gold-line:#8a5a1e;
  }
  *{box-sizing:border-box;margin:0;padding:0}
  html,body{width:801px;height:1200px;overflow:hidden}
  body{background:var(--bg);font-family:'Montserrat',sans-serif;position:relative;color:var(--ink)}
  .spread{position:absolute;left:66px;width:653px;height:504px;overflow:hidden;box-shadow:0 4px 14px rgba(0,0,0,.35)}
  .spread--cover{top:77px;background:var(--black)}
  .spread--inside{top:611px;background:var(--paper)}
  .abs{position:absolute}

  /* cover */
  .brand-panel{left:0;top:0;width:196px;height:504px;overflow:hidden;background:linear-gradient(180deg,var(--red) 0%,#e0432a 55%,var(--orange) 100%)}
  .brand-ghost{left:18px;top:150px;width:165px;font-weight:700;font-size:22px;line-height:1.1;color:rgba(255,255,255,.16)}
  .brand-name{left:29px;top:292px;width:150px;font-weight:700;font-size:17px;line-height:1.1;color:#fff}
  .panel-tagline{left:29px;top:344px;width:140px;color:#fff;font-size:5.6px;line-height:1.4}
  .panel-tagline b{font-weight:800;display:block;font-size:5.8px}
  .cover-photo{left:196px;top:0;width:457px;height:504px;background:radial-gradient(ellipse at 55% 40%,#6b5a52 0%,#3d3533 35%,#141314 75%,#050505 100%)}
  .cover-brand{left:386px;top:66px;width:200px;text-align:center;font-weight:700;font-size:17px;line-height:1.1;color:#fff}
  .cover-script{left:338px;top:368px;width:300px;text-align:center;font-family:'Great Vibes',cursive;font-size:15px;color:#fff}
  .cover-headline{left:338px;top:387px;width:300px;text-align:center;font-weight:800;font-size:17px;background:linear-gradient(90deg,var(--red),var(--orange));-webkit-background-clip:text;background-clip:text;color:transparent}
  .big-picture{left:362px;top:420px;width:255px;height:34px;border:1px solid var(--gold-line);display:flex;align-items:center}
  .big-picture__label{position:absolute;top:-4px;left:50%;transform:translateX(-50%);background:#0a0a0a;padding:0 5px;font-size:3.8px;font-weight:700;letter-spacing:.5px;color:#ddd}
  .stat{flex:1;text-align:center;color:#fff;font-size:8px;line-height:1.15;border-right:1px solid var(--gold-line)}
  .stat:last-child{border-right:0}
  .stat strong{display:block;font-weight:700}
  .cover-note{left:362px;top:463px;width:255px;text-align:center;color:#fff;font-size:10px}

  /* inside */
  .photo--church{left:0;top:0;width:124px;height:466px;background:linear-gradient(180deg,#7e9cc9 0%,#b9c3d3 35%,#a17c6e 62%,#6b5a3d 100%)}
  .text-col{left:124px;top:0;width:203px;height:466px;padding:24px 34px 0 19px}
  .sec-title{font-size:9px;line-height:1.1;font-weight:400;color:var(--ink)}
  .sec-title em{font-style:normal;font-weight:600;color:var(--red);display:block}
  .body{font-size:5.6px;line-height:1.42;color:var(--ink-soft)}
  .heart-row{display:flex;gap:12px;margin-top:6px}
  .heart-row .body{width:58px;color:var(--ink)}
  .script-list{font-family:'Great Vibes',cursive;font-size:10px;line-height:1.05;color:var(--red);border-left:1px solid #ccc;padding-left:5px}
  .verse-box{margin-top:10px;border:1px dashed #bbb;border-radius:3px;padding:4px 5px;font-size:4.4px;line-height:1.45;color:var(--ink)}
  .verse-box p+p{margin-top:4px}
  .divider{height:5px;margin:12px 0 12px;background:radial-gradient(ellipse at 50% 0,rgba(0,0,0,.25),transparent 70%)}
  .section+.section{margin-top:11px}
  .section .body{margin-top:5px}
  .photo--pastor{left:328px;top:0;width:98px;height:206px;background:linear-gradient(180deg,#bcbcbc,#6a6a6a 60%,#3b3b3b)}
  .photo--volunteers{left:428px;top:0;width:99px;height:206px;background:linear-gradient(180deg,#d6d3cf,#9a9590 55%,#55514d)}
  .model{left:327px;top:206px;width:200px;height:260px;background:var(--paper-grey);padding:19px 20px 0 29px}
  .model .body{margin-top:6px;color:var(--ink)}
  .tier-label{margin-top:9px;font-size:5.5px;font-weight:700;color:var(--ink)}
  .tiers{margin-top:9px;width:152px;border-collapse:collapse;font-size:5.6px;color:var(--ink)}
  .tiers th{font-weight:600;text-align:left;padding:6px 0;border-top:1px solid #ccc;border-bottom:1px solid #ccc}
  .tiers td{padding:4px 0;border-bottom:1px solid #e2e2e2;line-height:1.3}
  .tiers td:not(:first-child),.tiers th:not(:first-child){text-align:center}
  .tiers td:last-child,.tiers th:last-child{text-align:right}
  .total-row{display:flex;gap:22px;margin-top:4px}
  .total-box{width:36px;height:23px;background:linear-gradient(90deg,var(--red),#e5552e);color:#fff;font-size:5.6px;font-weight:700;padding:4px 3px;line-height:1.3}
  .margin-note{font-size:3.4px;line-height:1.5;color:#666;list-style:none}
  .margin-note li.bullet::before{content:"";display:inline-block;width:2px;height:2px;border-radius:50%;background:var(--red);margin-right:2px;vertical-align:middle}
  .photo--singer{left:527px;top:0;width:126px;height:466px;background:radial-gradient(ellipse at 60% 55%,#8a7d74 0%,#3e3733 40%,#111 85%)}
  .footer{left:0;top:466px;width:653px;height:38px;background:var(--black);display:flex;align-items:center}
  .footer__item{display:flex;align-items:center;gap:12px;width:326px;padding-left:28px}
  .join{font-size:12px;font-weight:600;background:linear-gradient(90deg,var(--red),var(--orange));-webkit-background-clip:text;background-clip:text;color:transparent}
  .footer__text{color:#fff;font-size:5.8px;line-height:1.45}
  .footer__text b{font-weight:800;display:block}
</style>
</head>
<body>

<section class="spread spread--cover">
  <div class="abs brand-panel">
    <div class="abs brand-ghost">Meadowlight<br>Church</div>
    <div class="abs brand-name">Meadowlight<br>Church</div>
    <div class="abs panel-tagline"><b>PRAY. LISTEN. STEP FORWARD IN FAITH.</b>Together, we believe God will do more than we can ask or imagine.</div>
  </div>
  <div class="abs cover-photo" role="img" aria-label="Photo of church members embracing during a service"></div>
  <div class="abs cover-brand">Meadowlight<br>Church</div>
  <div class="abs cover-script">Faithful in the Small, Powerful Together.</div>
  <div class="abs cover-headline">$150,000 IN 12 MONTHS</div>
  <div class="abs big-picture">
    <span class="big-picture__label">THE BIG PICTURE</span>
    <div class="stat">Total Goal<strong>$150,000</strong></div>
    <div class="stat">Active Members<strong>appr. 150 people</strong></div>
    <div class="stat">Timeframe<strong>12 months</strong></div>
  </div>
  <div class="abs cover-note">That is $1,000 per person per year on average</div>
</section>

<section class="spread spread--inside">
  <div class="abs photo--church" role="img" aria-label="Photo of the church building with a Love Like Him banner"></div>

  <div class="abs text-col">
    <div class="section">
      <h2 class="sec-title">The Heart<em>of the Vision</em></h2>
      <div class="heart-row">
        <p class="body">We are restoring more than space. We are restoring a church where we</p>
        <div class="script-list">Love like Him<br>Live like Him<br>Lead like Him</div>
      </div>
      <div class="verse-box">
        <p>“Whoever is faithful in very little is also faithful in much.”<br>Luke 16:10</p>
        <p>“How good and pleasant it is when God’s people live together in unity.”<br>Psalm 133:1</p>
      </div>
    </div>
    <div class="divider"></div>
    <div class="section">
      <h2 class="sec-title">Stories of<em>What God Is Doing</em></h2>
      <p class="body">One Wednesday night, a woman went to visit another church, but they were closed for a break. Instead of turning back, she came here. That unexpected moment became a divine appointment. God brought her to Meadowlight. Another couple walked through our doors carrying deep church hurt. From the very first moment, they felt seen, valued, and welcomed. What they found here was not just a service, but a family. This is what we are building together.</p>
      <p class="body">These gifts help build momentum, inspire others, and move the vision forward in powerful ways.</p>
    </div>
    <div class="section">
      <h2 class="sec-title">How We Move<em>Forward Together</em></h2>
      <p class="body">We encourage everyone to participate, even one dollar a day matters. Some to give stretch gifts as they are able. A few to provide leadership gifts to help anchor the campaign</p>
    </div>
    <div class="section">
      <h2 class="sec-title">A Shared<em>Commitment</em></h2>
      <p class="body">“If each of us gave just $20 a week, we would not only meet our goal, we would exceed it. But this is not about equal giving. It is about equal sacrifice. Some can give more, some less, but together, we can do something powerful.”</p>
    </div>
  </div>

  <div class="abs photo--pastor" role="img" aria-label="Black and white photo of the pastor preaching"></div>
  <div class="abs photo--volunteers" role="img" aria-label="Black and white photo of volunteers with donated groceries"></div>

  <div class="abs model">
    <h2 class="sec-title">Realistic<em>Participation Model</em></h2>
    <p class="body">Not everyone will give equally—so let’s build a real-world scenario:</p>
    <p class="tier-label">TIERED GIVING PLAN</p>
    <table class="tiers">
      <thead><tr><th>Group</th><th>People</th><th>Weekly Gift</th><th>Yearly Total</th></tr></thead>
      <tbody>
        <tr><td>Leadership<br>Givers</td><td>10</td><td>$100</td><td>$52,000</td></tr>
        <tr><td>Core<br>Givers</td><td>40</td><td>$40</td><td>$83,200</td></tr>
        <tr><td>Consistent<br>Givers</td><td>60</td><td>$20</td><td>$62,400</td></tr>
        <tr><td>Entry<br>Givers</td><td>40</td><td>$10</td><td>$20,800</td></tr>
      </tbody>
    </table>
    <div class="total-row">
      <div class="total-box">Total:<br>$218,400</div>
      <ul class="margin-note">
        <li>This exceeds the goal, giving margin for:</li>
        <li class="bullet">Missed weeks</li>
        <li class="bullet">Lower participation</li>
        <li class="bullet">Unexpected needs</li>
      </ul>
    </div>
  </div>

  <div class="abs photo--singer" role="img" aria-label="Black and white photo of a worship singer holding a microphone"></div>

  <footer class="abs footer">
    <div class="footer__item"><span class="join">Join Us</span><p class="footer__text"><b>PRAY. LISTEN. STEP FORWARD IN FAITH.</b>Together, we believe God will do more than we can ask or imagine.</p></div>
    <div class="footer__item"><span class="join">Join Us</span><p class="footer__text"><b>PRAY. LISTEN. STEP FORWARD IN FAITH.</b>Together, we believe God will do more than we can ask or imagine.</p></div>
  </footer>
</section>

</body>
</html>
```